Postcard Design

Postcard for the following:

Front of postcard:
A new little beauty and health haven has opened up just around the corner at 42 Marston Lane, Fernwood Rise.
Just like you, Mabel’s Lantern is special, offering treatments and services tailor made to your specific needs. Mabel has over 24 years of industry experience and offers a unique approach to helping you feel healthful, nourished and happy. Her treatments are brilliantly effective and include remedial massage therapies and reflexology, gorgeous rejuvenating facials and much much more…………..come and experience this unique and 100% organic little piece of heaven.
You deserve to feel great so we work from the inside out by offering nutritional health advice and formulations developed especially for you. We wholly nourish the individual in the wise woman tradition of healing and happiness.
As a special welcome gift I would like to offer you $15 off any service
By appointment 027 5162930 I look forward to seeing you soon

Back of postcard:
The hearth has been the centre of human life for at least 400,000 years. it is the place where people meet to cook, eat, talk together and heal. The ' hearth' was the heart of the home It was the centre of activity, where everyone gathered to keep warm, laugh, listen to the stories of old and heal. It was the place of physical and emotional nourishment. The hearth is a symbol for the hospitality and living spirit of the home.

Industry/Entity Type

Hospitality

Requirements
Nice to have
• A logo for the business would be really good.

```html
<!DOCTYPE html>
<html lang="en">
<head>
<meta charset="utf-8">
<title>Mabel’s Lantern Postcard</title>
<link href="https://fonts.googleapis.com/css2?family=Courgette&family=Didact+Gothic&family=EB+Garamond:wght@500&display=swap" rel="stylesheet">
<style>
  :root {
    --stage: #000000;
    --card-white: #ffffff;
    --rose: #e9659a;
    --rose-band: rgba(236, 130, 170, 0.78);
    --ink: #3a3436;
    --cocoa: #2e2420;
    --ember: #8a5a3c;
    --smoke: rgba(40, 26, 20, 0.72);
    --cream: #f4ece6;
    --script: "Courgette", cursive;
    --sans: "Didact Gothic", sans-serif;
    --serif: "EB Garamond", serif;
  }
  * { box-sizing: border-box; margin: 0; padding: 0; }
  html, body { width: 1126px; height: 1200px; overflow: hidden; background: var(--stage); }

  .postcard { position: absolute; overflow: hidden; }

  /* Front */
  .front { left: 40px; top: 40px; width: 740px; height: 540px; background: var(--card-white); }
  .front-intro {
    position: absolute; left: 30px; right: 30px; top: 34px;
    font-family: var(--sans); font-size: 15.5px; line-height: 1.5; color: var(--ink);
    text-align: center; z-index: 2;
  }
  .brand-name { font-family: var(--script); color: var(--rose); font-size: 27px; line-height: 1; }
  .spa-photo {
    position: absolute; left: 0; right: 0; top: 230px; bottom: 0;
    background:
      radial-gradient(ellipse 180px 130px at 190px 170px, rgba(240,160,90,0.85), transparent 70%),
      radial-gradient(ellipse 200px 110px at 180px 120px, rgba(130,70,50,0.7), transparent 72%),
      radial-gradient(ellipse 240px 150px at 470px 130px, #f3f1ef, transparent 75%),
      linear-gradient(180deg, #ffffff 0%, #ede7e3 40%, #e4dcd8 100%);
  }
  .haven-note {
    position: absolute; left: 410px; top: 290px; width: 310px;
    text-align: center; color: var(--cocoa); z-index: 2;
  }
  .haven-note .lead { font-family: var(--script); font-size: 22px; line-height: 1.2; }
  .haven-note .address { font-family: var(--serif); font-size: 21px; margin-top: 2px; }
  .rose-band { position: absolute; left: 0; bottom: 0; width: 740px; height: 150px; z-index: 1; }
  .welcome {
    position: absolute; left: 0; right: 0; bottom: 22px; z-index: 2;
    color: var(--cocoa); text-align: center;
  }
  .welcome .gift-title { font-family: var(--script); font-size: 22px; text-align: left; padding-left: 80px; }
  .welcome .offer { font-family: var(--serif); font-size: 20px; line-height: 1.3; }

  /* Back */
  .back { left: 386px; top: 630px; width: 700px; height: 540px; }
  .hearth-photo {
    position: absolute; inset: 0;
    background:
      radial-gradient(ellipse 120px 70px at 290px 175px, #f7c54a, #e2452c 55%, transparent 100%),
      radial-gradient(ellipse 250px 200px at 290px 200px, rgba(150,100,70,0.9), transparent 80%),
      linear-gradient(180deg, #6b4a36 0%, #4a3224 60%, #2e1f17 100%);
  }
  .hearth-story {
    position: absolute; left: 0; right: 0; top: 292px; height: 210px;
    background: var(--smoke); color: var(--cream);
    font-family: var(--sans); font-size: 15.5px; line-height: 1.62; text-align: center;
    padding-top: 18px;
  }
  .hearth-word { font-family: var(--script); color: var(--rose); font-size: 25px; line-height: 1; }
</style>
</head>
<body>

<section class="postcard front">
  <div class="spa-photo" role="img" aria-label="Spa still life: white orchid, wooden bowl of dried petals, lit orange candle and rolled white towels"></div>

  <p class="front-intro">
    Just like you, <span class="brand-name">Mabel’s Lantern</span> is special, offering treatments and services tailor
    made to your specific needs. Mabel has over 24 years of industry experience and offers a
    unique approach to helping you feel healthful, nourished and happy. Her treatments are
    brilliantly effective and include remedial massage therapies and reflexology, gorgeous
    rejuvenating facials and much much more…………..come and experience this unique and 100%
    organic little piece of heaven. You deserve to feel great so we work from the inside out by
    offering nutritional health advice and formulations developed especially for you.
    We wholly nourish the individual in the wise woman tradition of healing and happiness.
  </p>

  <div class="haven-note">
    <p class="lead">A new little beauty and health haven has opened up just around the corner at</p>
    <p class="address">42 Marston Lane, Fernwood Rise.</p>
  </div>

  <svg class="rose-band" viewBox="0 0 740 150" preserveAspectRatio="none" aria-hidden="true">
    <path d="M0 70 C 200 30, 420 30, 740 0 L 740 150 L 0 150 Z" fill="var(--rose-band)"/>
  </svg>

  <div class="welcome">
    <p class="gift-title">As a special welcome gift,</p>
    <p class="offer">I would like to offer you $15 off any service<br>
      By appointment 027 5162930. I look forward to seeing you soon</p>
  </div>
</section>

<section class="postcard back">
  <div class="hearth-photo" role="img" aria-label="Cast iron wood stove with a glowing fire against a brick wall, warm candlelit tones"></div>
  <div class="hearth-story">
    <p>The <span class="hearth-word">hearth</span> has been the centre of human life for at least 400,000 years.<br>
    it is the place where people meet to cook, eat and talk together and heal.<br>
    The ‘hearth’ was the heart of the home.<br>
    It was the centre of activity, where everyone gathered to eat and cook,<br>
    to sit and warm themselves, and listen to the stories of old.<br>
    It was the place of physical and emotional nourishment hearth is a symbol for<br>
    the hospitality and living spirit of the home</p>
  </div>
</section>

</body>
</html>
```